Business Card Design for a new Senior Concierge Business 1.3.24

I need a professional business card to handout at networking events for my senior helper business. I would like to use the logo I have uploaded. The design should be clear and easy to read and should list the following information...
Dessa Kirwin
Owner
www.BrightwellElderAides.example
Fenwick Hollow, Ohio
555.248.3906
Dessa@brightwellelderaides.example

Target Market(s)

Senior Citizens

Industry/Entity Type

Personal Helper/ Assisstant

Contact Information for Business Card

I have included the details in the project description box.

Font styles to use
Serif

Colors
0054AA
0677BA
7BADD7
CADEEF
E8F1F8
59FF00
82FF00
B8FF75
E3FFCB
F4FFEA
E54698
E96AAD
F1A4CE
F9D9EA
FCEFF6
6B429C
8869AF
B7A5CE
E3DAEB
F3F0F8

Requirements
Must have
• Include uploaded logo
Nice to have
• The log that has been uploaded
Should not have
• No crazy fonts

```html
<!DOCTYPE html>
<html lang="en">
<head>
<meta charset="utf-8">
<title>Brightwell Elder Aides – Business Card</title>
<link rel="stylesheet" href="https://fonts.googleapis.com/css2?family=Open+Sans:wght@400;600;700&display=swap">
<style>
  :root {
    --backdrop: #2a2a2c;
    --card: #222226;
    --card-edge: #1a1a1d;
    --emboss: #17171a;
    --violet: #6b55b0;
    --pink: #e0195f;
    --teal: #13939a;
    --white: #f2f2f2;
    --rule: #e8e8e8;
  }
  * { box-sizing: border-box; margin: 0; padding: 0; }
  html, body {
    width: 1200px; height: 779px; overflow: hidden;
    background: var(--backdrop);
    font-family: "Open Sans", Arial, sans-serif;
  }
  .stage {
    width: 1200px; height: 779px;
    display: flex; align-items: center; justify-content: center; gap: 40px;
  }
  .card {
    position: relative;
    width: 540px; height: 309px;
    background: var(--card);
    overflow: hidden;
    box-shadow: 0 14px 30px rgba(0,0,0,.55);
  }
  /* back side */
  .card-back { display: flex; align-items: center; justify-content: center; gap: 14px; }
  .card-back .brand-mark {
    width: 30px; height: 30px; border-radius: 50%;
    background: var(--emboss);
  }
  .card-back .brand-name {
    font-size: 40px; font-weight: 600; color: var(--emboss);
    letter-spacing: .5px;
  }
  /* front side */
  .brand {
    position: absolute; left: 34px; top: 38px;
    display: flex; align-items: center; gap: 10px;
  }
  .brand .brand-mark {
    width: 20px; height: 20px; border-radius: 50%; background: var(--violet);
  }
  .brand .brand-name {
    font-size: 24px; font-weight: 400; color: var(--violet);
  }
  .divider {
    position: absolute; left: 86px; right: 40px; top: 150px;
    height: 1px; background: var(--rule);
  }
  .holder {
    position: absolute; right: 40px; top: 96px; text-align: right;
  }
  .holder-name { font-size: 26px; font-weight: 700; line-height: 1.1; }
  .holder-name .first { color: var(--teal); }
  .holder-name .last { color: var(--pink); }
  .holder-role { font-size: 12px; color: var(--white); margin-top: 2px; }
  .tab {
    position: absolute; right: 0; top: 92px;
    width: 26px; height: 34px; background: var(--pink);
  }
  .details {
    position: absolute; left: 40px; top: 174px;
    color: var(--white); font-size: 13px;
  }
  .details .city { margin-bottom: 12px; }
  .details ul { list-style: none; }
  .details li { display: flex; align-items: center; gap: 8px; line-height: 19px; }
  .details svg { width: 12px; height: 12px; flex: none; }
  .swoosh { position: absolute; left: 0; bottom: 0; width: 540px; height: 309px; }
</style>
</head>
<body>
<main class="stage">
  <section class="card card-back" aria-label="Card back">
    <span class="brand-mark"></span>
    <span class="brand-name">Brightwell Elder Aides</span>
  </section>

  <section class="card card-front" aria-label="Card front">
    <svg class="swoosh" viewBox="0 0 540 309" aria-hidden="true">
      <path d="M290 309 C 360 235, 450 200, 540 186 L540 309 Z" fill="var(--pink)"/>
      <path d="M360 309 C 410 255, 478 222, 540 211 L540 309 Z" fill="var(--card-edge)"/>
      <path d="M374 309 C 420 262, 482 229, 540 218 L540 309 Z" fill="var(--teal)"/>
    </svg>

    <div class="brand">
      <span class="brand-mark"></span>
      <span class="brand-name">Brightwell Elder Aides</span>
    </div>

    <div class="tab"></div>
    <div class="holder">
      <p class="holder-name"><span class="first">Dessa</span> <span class="last">Kirwin</span></p>
      <p class="holder-role">Owner</p>
    </div>

    <div class="divider"></div>

    <div class="details">
      <p class="city">Fenwick Hollow, Ohio</p>
      <ul>
        <li>
          <svg viewBox="0 0 24 24"><path fill="var(--teal)" d="M6.6 10.8a15 15 0 0 0 6.6 6.6l2.2-2.2a1 1 0 0 1 1-.25 11.4 11.4 0 0 0 3.6.57 1 1 0 0 1 1 1V20a1 1 0 0 1-1 1A17 17 0 0 1 3 4a1 1 0 0 1 1-1h3.5a1 1 0 0 1 1 1c0 1.25.2 2.45.57 3.57a1 1 0 0 1-.25 1z"/></svg>
          555.248.3906
        </li>
        <li>
          <svg viewBox="0 0 24 24"><circle cx="12" cy="12" r="9" fill="none" stroke="var(--teal)" stroke-width="2.5"/><path d="M3 12h18M12 3c3 3 3 15 0 18M12 3c-3 3-3 15 0 18" fill="none" stroke="var(--teal)" stroke-width="2"/></svg>
          www.BrightwellElderAides.example
        </li>
        <li>
          <svg viewBox="0 0 24 24"><rect x="2" y="5" width="20" height="14" rx="2" fill="var(--teal)"/><path d="M3 6l9 7 9-7" fill="none" stroke="var(--card)" stroke-width="2"/></svg>
          Dessa@brightwellelderaides.example
        </li>
      </ul>
    </div>
  </section>
</main>
</body>
</html>
```